Letterhead Design

I would like 2 different letterheads. One with each logo I have attached. Business info:
Larkfield Medical Billing, LLC
3870 N Cedar
Ossing, KS 66492
(866) 555-0143

```html
<!DOCTYPE html>
<html lang="en">
<head>
<meta charset="utf-8">
<title>Larkfield Medical Billing – Letterhead</title>
<link href="https://fonts.googleapis.com/css2?family=Marcellus+SC&family=Arimo:wght@400;700&display=swap" rel="stylesheet">
<style>
  :root {
    --backdrop: #e9e9e9;
    --paper: #f7f7f7;
    --band: #0f4a63;
    --ink: #1f2a30;
    --brand: #1d5a70;
    --mark: #2b9aa2;
    --watermark: rgba(70, 80, 85, 0.09);
  }
  html, body {
    margin: 0;
    padding: 0;
    width: 1200px;
    height: 1028px;
    overflow: hidden;
    background: var(--backdrop);
  }
  .letterhead {
    position: absolute;
    left: 290px;
    top: 84px;
    width: 620px;
    height: 860px;
    background: var(--paper);
    box-shadow: 0 10px 30px rgba(0,0,0,0.12);
  }
  .letterhead__band {
    position: absolute;
    left: 0;
    right: 0;
    height: 7px;
    background: var(--band);
  }
  .letterhead__band--top { top: 0; }
  .letterhead__band--bottom { bottom: 0; }
  .brand {
    position: absolute;
    left: 40px;
    top: 40px;
    display: flex;
    align-items: center;
    gap: 8px;
    font-family: "Arimo", Arial, sans-serif;
    font-weight: 700;
    font-size: 15px;
    color: var(--mark);
    letter-spacing: 0.5px;
  }
  .brand__square {
    width: 14px;
    height: 14px;
    background: var(--mark);
  }
  .sender {
    position: absolute;
    right: 40px;
    top: 34px;
    text-align: right;
  }
  .sender__name {
    font-family: "Marcellus SC", Georgia, serif;
    font-size: 19px;
    color: var(--brand);
    letter-spacing: 0.6px;
    margin: 0 0 10px;
  }
  .sender__line {
    font-family: "Arimo", Arial, sans-serif;
    font-size: 12px;
    color: var(--ink);
    margin: 2px 0;
    display: flex;
    justify-content: flex-end;
    align-items: center;
    gap: 6px;
  }
  .sender__icon { width: 10px; height: 10px; }
  .watermark {
    position: absolute;
    left: 0;
    right: 0;
    top: 380px;
    text-align: center;
    font-family: "Marcellus SC", Georgia, serif;
    font-size: 54px;
    line-height: 1.1;
    color: var(--watermark);
  }
</style>
</head>
<body>
  <main class="letterhead">
    <div class="letterhead__band letterhead__band--top"></div>

    <div class="brand">
      <span class="brand__square"></span>
      <span class="brand__name">Larkfield</span>
    </div>

    <header class="sender">
      <p class="sender__name">Larkfield Medical Billing, LLC</p>
      <p class="sender__line">3870 N Cedar
        <svg class="sender__icon" viewBox="0 0 10 10" aria-hidden="true"><path d="M5 0.5a3.2 3.2 0 0 0-3.2 3.2C1.8 6 5 9.5 5 9.5S8.2 6 8.2 3.7A3.2 3.2 0 0 0 5 0.5zm0 4.4a1.2 1.2 0 1 1 0-2.4 1.2 1.2 0 0 1 0 2.4z" fill="#1f2a30"/></svg>
      </p>
      <p class="sender__line">Ossing, KS 66492
        <svg class="sender__icon" viewBox="0 0 10 10" aria-hidden="true"></svg>
      </p>
      <p class="sender__line">(866) 555-0143
        <svg class="sender__icon" viewBox="0 0 10 10" aria-hidden="true"><path d="M2.2 0.8l1.6 1.9-0.9 1.2c0.6 1.3 1.6 2.3 2.9 2.9l1.2-0.9 1.9 1.6-0.9 1.5C4.6 8.8 1.2 5.4 0.8 1.7z" fill="#1f2a30"/></svg>
      </p>
    </header>

    <div class="watermark" aria-hidden="true">Larkfield<br>Medical Billing</div>

    <div class="letterhead__band letterhead__band--bottom"></div>
  </main>
</body>
</html>
```